Business Card for IT company

I need a high tech looking business card using our logo. I prefer something clean and modern.

Target Market(s)

Buyers of IT hardware and software, IT Techies who are key influencers

Industry/Entity Type

Business

```html
<!DOCTYPE html>
<html lang="en">
<head>
<meta charset="utf-8">
<title>KVRA Consulting – Business Card</title>
<link rel="stylesheet" href="https://fonts.googleapis.com/css2?family=Oxanium:wght@400;500&display=swap">
<style>
  :root {
    --card-bg: #070908;
    --band-tone: #1d251e;
    --accent: #62e21a;
    --brand: #f2f4f2;
  }
  html, body {
    margin: 0;
    padding: 0;
    width: 1200px;
    height: 720px;
    overflow: hidden;
    background: var(--card-bg);
  }
  .card {
    position: relative;
    width: 1200px;
    height: 720px;
    background: var(--card-bg);
    overflow: hidden;
    font-family: "Oxanium", sans-serif;
  }
  .decor-band {
    position: absolute;
    left: 0;
    top: 340px;
    width: 1160px;
    height: 355px;
    border-radius: 0 22px 22px 0;
    background: linear-gradient(180deg, rgba(29, 37, 30, 0.85) 0%, rgba(29, 37, 30, 0.55) 55%, rgba(29, 37, 30, 0.25) 100%);
  }
  .brand-name,
  .contact-block {
    position: absolute;
    left: 0;
    top: 0;
    width: 1200px;
    height: 720px;
  }
  .brand-name text {
    fill: var(--brand);
    font-family: "Oxanium", sans-serif;
    font-weight: 500;
  }
  .contact-block text {
    fill: var(--accent);
    font-family: "Oxanium", sans-serif;
    font-weight: 400;
  }
  .contact-block .label { font-variant: small-caps; }
</style>
</head>
<body>
  <div class="card">
    <div class="decor-band" role="img" aria-label="Circuit-board trace pattern in dark green-grey"></div>

    <svg class="brand-name" viewBox="0 0 1200 720" role="img" aria-label="KVRA Consulting">
      <text x="102" y="238" font-size="190" textLength="612" lengthAdjust="spacingAndGlyphs">KVRA</text>
      <text x="104" y="306" font-size="62" textLength="610" lengthAdjust="spacing">CONSULTING</text>
    </svg>

    <svg class="contact-block" viewBox="0 0 1200 720">
      <text x="512" y="542" font-size="64" textLength="580" lengthAdjust="spacingAndGlyphs"><tspan class="label">Name</tspan> Mark Olsen</text>
      <text x="606" y="580" font-size="38" textLength="518" lengthAdjust="spacingAndGlyphs"><tspan class="label">Title</tspan> Operation Manager</text>
      <text x="587" y="614" font-size="38" textLength="404" lengthAdjust="spacingAndGlyphs"><tspan class="label">Phone</tspan> 1-555-017290</text>
      <text x="590" y="648" font-size="38" textLength="410" lengthAdjust="spacingAndGlyphs"><tspan class="label">Email</tspan> <tspan font-size="27">mark@kvra.example</tspan></text>
    </svg>
  </div>
</body>
</html>
```